MOLVIKAN Hemp based Pet Brand that growns it's own premium hemp and creates amazing pet products.

We need packaging designed for a new company based in South West Florida. We grow our own hemp with our other company Fern 9 Vat and use the harvest to make our hemp based pet products. Our initial products are pet treats that include Soft Chews and Calming Chews. The bags come in two different sizes. Regular bag being 7x10.25 inches and Small bag 4.25X6.25 inches. We also need a tincture box and label created. We want packaging that will catch the eye of the consumer and colors that compliment our logo. Dropper label size is 4x1.75 inches and the milligram of CBD is 1500. We have attached our manufacturers packaging and would like you to coppy everything other than their overall design and logo. Use default UPC and QR code, which we can replace later in the Ai file. Please see all the attached documents and please ask me if you have any questions. The final design should communicate a premium product that stand our from the rest. Something that catches the eye of the consumer by its premium appearance. Packaging is everything so I hope you can use your creative skills to create something special!

Target Market(s)

Pet owners

Font styles to use
Serif
Sans Serif

Colors
0054AA
0677BA
7BADD7
CADEEF
E8F1F8
0094D4
00A9DD
6FCCEA
C7EBF8
E9F6FB
EE7325
F08F49
F5BC92
FAE3D3
FDF4ED

Requirements
Must have
• Stand out design. Premium feel. Imagine shopping for something for your pet and seeing a brand that POPS and just looks like a good product because the packaging is so good.
Nice to have
• Modern mature feel
Should not have
• Cartoony feeling. Do not use baby blue everywhere. Do not include pictures of people in the packaging

```html
<!DOCTYPE html>
<html lang="en">
<head>
<meta charset="utf-8">
<title>MOLVIKAN Calming Chews – Pouch Front</title>
<link rel="stylesheet" href="https://fonts.googleapis.com/css2?family=Bebas+Neue&family=Oswald:wght@500&family=Poppins:wght@500&display=swap">
<style>
  :root {
    --stage: #bdbdbd;
    --navy: #1b3263;
    --navy-deep: #0f1d3d;
    --steel: #4a6f97;
    --orange: #ee7325;
    --orange-soft: #f08f49;
    --peach: #f5bc92;
    --sky: #0094d4;
    --ice: #c7ebf8;
    --white: #ffffff;
  }
  * { margin: 0; padding: 0; box-sizing: border-box; }
  html, body { width: 1200px; height: 800px; overflow: hidden; }
  body { background: var(--stage); position: relative; }

  .pouch-front {
    position: absolute;
    left: 360px; top: 55px;
    width: 480px; height: 690px;
    overflow: hidden;
  }
  .pattern-field {
    position: absolute; inset: 0;
    background:
      linear-gradient(135deg, var(--ice) 0%, var(--sky) 22%, var(--orange-soft) 45%, var(--navy) 60%, var(--orange) 78%, var(--ice) 100%);
  }
  .center-column {
    position: absolute;
    left: 135px; top: 155px;
    width: 210px; height: 535px;
    background: linear-gradient(180deg, var(--navy) 0%, var(--navy-deep) 55%, var(--navy) 100%);
  }
  .brand-badge {
    position: absolute;
    left: 150px; top: 170px;
    width: 180px; height: 180px;
    border-radius: 50%;
    background: var(--ice);
    border: 4px solid var(--white);
    display: flex; align-items: center; justify-content: center;
  }
  .brand-name {
    font-family: "Bebas Neue", sans-serif;
    font-size: 38px;
    letter-spacing: 2px;
    color: var(--navy-deep);
  }
  .product-title {
    position: absolute;
    left: 0; width: 480px; top: 378px;
    text-align: center;
    font-family: "Bebas Neue", sans-serif;
    color: var(--white);
    line-height: 0.92;
  }
  .product-title .line-one { display: block; font-size: 58px; letter-spacing: 1px; }
  .product-title .line-two { display: block; font-size: 58px; letter-spacing: 1px; }
  .tagline-bone {
    position: absolute;
    left: 165px; top: 491px;
    width: 150px; height: 50px;
  }
  .tagline-bone svg { position: absolute; inset: 0; }
  .tagline-text {
    position: absolute; inset: 0;
    display: flex; align-items: center; justify-content: center;
    font-family: "Poppins", sans-serif;
    font-size: 11.5px;
    color: var(--white);
  }
  .net-contents {
    position: absolute;
    left: 0; width: 480px; top: 570px;
    text-align: center;
    font-family: "Oswald", sans-serif;
    font-weight: 500;
    font-size: 17px;
    line-height: 1.2;
    color: var(--white);
  }
</style>
</head>
<body>
  <main class="pouch-front">
    <div class="pattern-field" role="img" aria-label="Geometric pattern of orange, navy, sky blue and white blocks, triangles and quarter circles framing the panel"></div>
    <div class="center-column"></div>

    <div class="brand-badge">
      <span class="brand-name">MOLVIKAN</span>
    </div>

    <h1 class="product-title">
      <span class="line-one">Calming</span>
      <span class="line-two">Chews</span>
    </h1>

    <div class="tagline-bone">
      <svg viewBox="0 0 150 50" width="150" height="50" aria-hidden="true">
        <g fill="var(--orange-soft)" stroke="var(--orange)" stroke-width="2">
          <path d="M22 12 A12 12 0 1 1 14 25 A12 12 0 1 1 22 38 L128 38 A12 12 0 1 1 136 25 A12 12 0 1 1 128 12 Z"/>
        </g>
      </svg>
      <span class="tagline-text">Lorem ipsum dolor</span>
    </div>

    <p class="net-contents">Net CT 60<br>Net Wt. 10.5 oz</p>
  </main>
</body>
</html>
```